Happy Birthday Postcard for law firm for existing clients

Need a postcard that will go out to our current clients on their birthdays. Prefer to have our logo incorporated as part of the design so it reminds them about our business. The back needs to say "Happy Birthday from the team at Dunmore Law Firm."

We are a law firm that services local clients. Needs to be mailed so the backside right half needs to be left blank except the return address (in NEEDS below) so it can be mailed with a mailing label.

Target Market(s)

existing customers, varying age range and demographic profile

Industry/Entity Type

Legal

Font styles to use
Sans Serif
Script

Colors

Designer to choose colors to be used in the design.

Requirements
Must have
• Our logo preferrably on the front (can be modified or added to so it fits a birthday message. And needs to be mailed so the back right side needs to be left open for address labels. The firms return address is
• Dunmore Law Firm
• 4718 W Pebblecrest Ave
• Springfield, MO 65917
• Needs to have the text included in the project description on the back, or some close iteration of it if space is limited.
Nice to have
• Some illustration or graphic on the front with the logo that shows it is a birthday postcard

```html
<!DOCTYPE html>
<html lang="en">
<head>
<meta charset="utf-8">
<title>Dunmore Law Firm – Birthday Postcard</title>
<link rel="stylesheet" href="https://fonts.googleapis.com/css2?family=Cinzel:wght@400;700&family=Josefin+Sans:wght@300;400;600&family=Lobster&display=swap">
<style>
  :root {
    --stage: #0a6fbd;
    --card-white: #ffffff;
    --party-pink: #d98bb8;
    --party-blue: #8fb3d6;
    --party-lilac: #b58cc2;
    --ring-lilac: #a57bb3;
    --headline-pink: #e0288a;
    --panel-lavender: #9ba3c8;
    --panel-shade: #8a93bb;
    --ink-grey: #4a4a55;
    --line-grey: #9a9a9a;
    --stamp-border: #c8c8c8;
  }
  * { box-sizing: border-box; margin: 0; padding: 0; }
  html, body { width: 800px; height: 1200px; overflow: hidden; }
  body { background: var(--stage); position: relative; }

  .postcard { position: absolute; left: 96px; width: 608px; height: 474px; overflow: hidden; background: var(--card-white); }
  .postcard--front { top: 97px; }
  .postcard--back { top: 630px; }

  /* Front */
  .party-backdrop {
    position: absolute; inset: 0;
    background:
      radial-gradient(ellipse at 50% 35%, rgba(240,170,210,0.55), transparent 60%),
      linear-gradient(160deg, var(--party-pink) 0%, var(--party-lilac) 45%, var(--party-blue) 75%, var(--party-pink) 100%);
  }
  .logo-seal { position: absolute; left: 188px; top: 38px; width: 232px; height: 232px; }
  .logo-name {
    position: absolute; left: 0; right: 0; top: 170px; text-align: center;
    font-family: "Josefin Sans", sans-serif; font-weight: 400; font-size: 22px;
    letter-spacing: 1px; color: var(--ink-grey);
  }
  .greeting {
    position: absolute; left: 0; right: 0; top: 272px; text-align: center;
    font-family: "Lobster", cursive; font-size: 58px; color: #fff;
    -webkit-text-stroke: 2px var(--headline-pink); paint-order: stroke fill;
    text-shadow: 0 0 0 var(--headline-pink);
  }
  .greeting-sub {
    position: absolute; left: 0; right: 0; top: 365px; text-align: center;
    font-family: "Cinzel", serif; font-weight: 700; font-size: 21px; letter-spacing: 1px; color: #fff;
  }
  .firm-name {
    position: absolute; left: 0; right: 0; top: 397px; text-align: center;
    font-family: "Josefin Sans", sans-serif; font-weight: 300; font-size: 38px; color: #fff;
  }
  .firm-name strong { font-weight: 600; }

  /* Back */
  .message-panel {
    position: absolute; left: 0; top: 0; width: 306px; height: 474px;
    background: linear-gradient(180deg, var(--panel-lavender), var(--panel-shade));
  }
  .tagline-lead { position: absolute; left: 15px; top: 46px; font-family: "Cinzel", serif; font-size: 18px; color: #fff; }
  .tagline-main { position: absolute; left: 14px; top: 68px; font-family: "Cinzel", serif; font-weight: 700; font-size: 28px; color: #fff; }
  .contact-label { position: absolute; left: 13px; font-family: "Cinzel", serif; color: #fff; }
  .contact-label--call { top: 114px; font-size: 38px; }
  .contact-label--toll { top: 205px; left: 16px; font-size: 24px; }
  .contact-number { position: absolute; left: 15px; font-family: "Cinzel", serif; font-size: 26px; color: #fff; }
  .contact-number--call { top: 152px; }
  .contact-number--toll { top: 240px; }
  .return-address {
    position: absolute; left: 72px; top: 331px; width: 152px; height: 104px;
    background: var(--card-white); border-radius: 3px; text-align: center; padding-top: 40px;
  }
  .return-address__name { font-family: "Josefin Sans", sans-serif; font-size: 16px; color: var(--ink-grey); }
  .return-address__line { font-family: "Josefin Sans", sans-serif; font-size: 10px; line-height: 13px; color: var(--ink-grey); }
  .stamp-box { position: absolute; left: 446px; top: 34px; width: 142px; height: 128px; border: 1px solid var(--stamp-border); border-radius: 3px; }
  .address-line { position: absolute; left: 323px; width: 265px; border-top: 1px dotted var(--line-grey); }
</style>
</head>
<body>

<section class="postcard postcard--front">
  <div class="party-backdrop" role="img" aria-label="Birthday scene with lit candles, confetti and streamers behind pink and blue sunburst rays"></div>
  <svg class="logo-seal" viewBox="0 0 232 232" aria-hidden="true">
    <circle cx="116" cy="116" r="114" fill="none" stroke="var(--ring-lilac)" stroke-width="1.5"/>
    <circle cx="116" cy="116" r="110" fill="var(--ring-lilac)"/>
    <circle cx="116" cy="116" r="106" fill="none" stroke="#fff" stroke-width="2" stroke-dasharray="1 5" stroke-linecap="round"/>
    <circle cx="116" cy="116" r="101" fill="#fff"/>
  </svg>
  <div class="logo-name">DUNMORE LAW</div>
  <h1 class="greeting">Happy Birthday</h1>
  <p class="greeting-sub">FROM THE TEAM AT</p>
  <p class="firm-name"><strong>DUNMORE</strong> LAW FIRM</p>
</section>

<section class="postcard postcard--back">
  <div class="message-panel" role="img" aria-label="Lavender-toned photo of an attorney in shirt and tie in an office"></div>
  <p class="tagline-lead">Its About Taking</p>
  <p class="tagline-main">Responsibility</p>
  <p class="contact-label contact-label--call">Call Us:</p>
  <p class="contact-number contact-number--call">(417) 555-0142</p>
  <p class="contact-label contact-label--toll">Toll Free:</p>
  <p class="contact-number contact-number--toll">1-800-555-0199</p>
  <div class="return-address">
    <p class="return-address__name">DUNMORE LAW</p>
    <p class="return-address__line">4718 W Pebblecrest Ave</p>
    <p class="return-address__line">Springfield, MO 65917</p>
  </div>
  <div class="stamp-box"></div>
  <div class="address-line" style="top:237px"></div>
  <div class="address-line" style="top:274px"></div>
  <div class="address-line" style="top:311px"></div>
  <div class="address-line" style="top:348px"></div>
  <div class="address-line" style="top:385px"></div>
</section>

</body>
</html>
```